Veltarum

Standard Business Card design.
Sample two-sided design uploaded. White front, Black back.
Would like white shield to be on all black background side.
Willing to look at a couple creative designs, but nothing crazy.
Preference for a classic, confident, strong design.

```html
<!DOCTYPE html>
<html lang="en">
<head>
<meta charset="UTF-8">
<title>Veltarum Business Card</title>
<link rel="stylesheet" href="https://fonts.googleapis.com/css2?family=Montserrat:wght@400;500;700&display=swap">
<style>
  :root {
    --backdrop: #9b9b9b;
    --card-white: #f7f7f5;
    --card-black: #141414;
    --ink: #1b1b1b;
    --ink-soft: #3a3a3a;
    --paper-white: #f2f2f2;
  }
  * { margin: 0; padding: 0; box-sizing: border-box; }
  html, body {
    width: 1200px;
    height: 956px;
    overflow: hidden;
    background: var(--backdrop);
    font-family: "Montserrat", sans-serif;
  }
  .canvas {
    width: 1200px;
    height: 956px;
    display: flex;
    flex-direction: column;
    align-items: center;
    justify-content: center;
    gap: 56px;
  }
  .card {
    width: 630px;
    height: 360px;
    position: relative;
    box-shadow: 0 10px 30px rgba(0,0,0,0.25);
  }
  .card--front { background: var(--card-white); color: var(--ink); }
  .card--back {
    background: var(--card-black);
    display: flex;
    align-items: center;
    justify-content: center;
  }
  .contact-block {
    position: absolute;
    left: 48px;
    top: 150px;
  }
  .contact-block__name {
    font-size: 30px;
    font-weight: 700;
    letter-spacing: 1.5px;
    line-height: 1;
  }
  .contact-block__title {
    font-size: 14px;
    font-weight: 400;
    letter-spacing: 1px;
    color: var(--ink-soft);
    margin-top: 4px;
    margin-bottom: 18px;
  }
  .contact-list { list-style: none; }
  .contact-list__item {
    display: flex;
    align-items: center;
    gap: 10px;
    font-size: 15px;
    letter-spacing: 0.6px;
    color: var(--ink);
    margin-bottom: 8px;
  }
  .contact-list__icon { width: 14px; height: 14px; flex: none; }
  .brand-lockup {
    position: absolute;
    right: 50px;
    top: 130px;
    font-size: 38px;
    font-weight: 700;
    letter-spacing: 4px;
    color: var(--ink);
    text-transform: uppercase;
  }
  .brand-back {
    font-size: 54px;
    font-weight: 700;
    letter-spacing: 6px;
    text-transform: uppercase;
    color: var(--paper-white);
  }
</style>
</head>
<body>
<main class="canvas">
  <section class="card card--front" aria-label="Card front">
    <div class="contact-block">
      <p class="contact-block__name">DANIEL HART</p>
      <p class="contact-block__title">MANAGER</p>
      <ul class="contact-list">
        <li class="contact-list__item">
          <svg class="contact-list__icon" viewBox="0 0 24 24" aria-hidden="true"><path fill="#1b1b1b" d="M6.6 10.8a15.1 15.1 0 0 0 6.6 6.6l2.2-2.2a1 1 0 0 1 1-.25 11.4 11.4 0 0 0 3.6.57 1 1 0 0 1 1 1V20a1 1 0 0 1-1 1A17 17 0 0 1 3 4a1 1 0 0 1 1-1h3.5a1 1 0 0 1 1 1c0 1.25.2 2.45.57 3.6a1 1 0 0 1-.25 1z"/></svg>
          (415)555-0142
        </li>
        <li class="contact-list__item">
          <svg class="contact-list__icon" viewBox="0 0 24 24" aria-hidden="true"><path fill="#1b1b1b" d="M2 5h20v14H2z"/><path fill="none" stroke="#f7f7f5" stroke-width="1.6" d="M2.5 5.5 12 13l9.5-7.5"/></svg>
          hello@veltarum.com
        </li>
        <li class="contact-list__item">
          <svg class="contact-list__icon" viewBox="0 0 24 24" aria-hidden="true"><g fill="none" stroke="#1b1b1b" stroke-width="1.8"><circle cx="12" cy="12" r="10"/><ellipse cx="12" cy="12" rx="4.5" ry="10"/><path d="M2 12h20M4 7h16M4 17h16"/></g></svg>
          www.veltarum.com
        </li>
      </ul>
    </div>
    <p class="brand-lockup">Veltarum</p>
  </section>

  <section class="card card--back" aria-label="Card back">
    <p class="brand-back">Veltarum</p>
  </section>
</main>
</body>
</html>
```